2025 Fall Auction

Large Farm and construction online only auction November 3rd thru 5Th
Bidding Closes November 5 th at 7 pm
Now Accepting Consignment call ( 555 )-271-6038 or email Marcus@brevlandsales.com
150 + Skid Steer Attachments
50 + Pieces of farm equipment
More To Come
Consignments are welcomed Till October 25Th

Target Market(s)

New customers

```html
<!DOCTYPE html>
<html lang="en">
<head>
<meta charset="utf-8">
<title>Large Farm &amp; Construction Online Only Auction</title>
<link href="https://fonts.googleapis.com/css2?family=Poppins:wght@300;400;600;700;800&display=swap" rel="stylesheet">
<style>
  :root {
    --backdrop: #7a7a7a;
    --charcoal: #252525;
    --orange: #f7931e;
    --white: #ffffff;
    --ink: #1b1b1b;
    --silver: #9a9a9a;
  }
  * { margin: 0; padding: 0; box-sizing: border-box; }
  html, body { width: 1200px; height: 681px; overflow: hidden; }
  body {
    background: var(--backdrop);
    font-family: "Poppins", sans-serif;
    display: flex; align-items: center; justify-content: center;
  }
  .flyer {
    position: relative;
    width: 466px; height: 660px;
    background: var(--charcoal);
    overflow: hidden;
    color: var(--white);
  }
  .hero-photo {
    position: absolute; left: 0; top: 0; width: 466px; height: 290px;
    background: linear-gradient(180deg, #5e6a4c 0%, #4d5a3a 35%, #3d4a2c 60%, #2c3322 85%, #1f221b 100%);
  }
  .shapes { position: absolute; left: 0; top: 0; width: 466px; height: 660px; }
  .brand {
    position: absolute; right: 20px; top: 72px;
    display: flex; align-items: center; gap: 6px;
    font-weight: 700; font-size: 13px; letter-spacing: .3px; color: var(--white);
  }
  .brand-dot { width: 14px; height: 14px; border-radius: 50%; background: var(--white); }
  .title {
    position: absolute; left: 0; width: 466px; text-align: center;
    font-weight: 800; line-height: 1; text-transform: uppercase;
    text-shadow: 0 2px 6px rgba(0,0,0,.45);
  }
  .title-line1 { top: 118px; font-size: 36px; }
  .title-line2 { top: 158px; font-size: 39px; }
  .subtitle {
    position: absolute; top: 203px; left: 0; width: 466px;
    display: flex; align-items: center; justify-content: center; gap: 9px;
    color: var(--orange); font-weight: 400; font-size: 21px; line-height: 1;
  }
  .subtitle-rule { width: 28px; height: 2px; background: var(--orange); }
  .feature-photo {
    position: absolute; left: 258px; top: 240px; width: 181px; height: 181px;
    border-radius: 50%; border: 3px solid var(--orange);
    background: radial-gradient(circle at 55% 50%, #5a5d66 0%, #3b3e46 35%, #ffffff 62%);
  }
  .dates { position: absolute; left: 29px; top: 298px; }
  .dates-month { color: var(--orange); font-weight: 600; font-size: 25px; line-height: 1; }
  .dates-range { font-weight: 400; font-size: 24px; line-height: 1.15; }
  .dates-range sup { font-size: 12px; }
  .closing {
    position: absolute; left: 28px; top: 368px;
    border-left: 2px solid var(--orange); padding-left: 7px;
    font-size: 15px; line-height: 1.3;
  }
  .closing-label { color: var(--orange); font-weight: 700; }
  .closing sup { font-size: 8px; }
  .consign-band {
    position: absolute; left: 0; top: 432px; width: 466px; height: 29px;
    background: var(--white); color: var(--orange);
    font-weight: 800; font-size: 22.5px; line-height: 29px; text-align: center;
  }
  .stat { position: absolute; top: 474px; line-height: 1; }
  .stat-number { color: var(--orange); font-weight: 800; font-size: 30px; }
  .stat-label { font-size: 15px; line-height: 1.25; margin-top: 3px; }
  .stat-attachments { left: 71px; }
  .stat-farm { left: 282px; }
  .stat-divider { position: absolute; left: 229px; top: 476px; width: 2px; height: 67px; background: var(--white); }
  .welcome-pill {
    position: absolute; left: 29px; top: 556px; width: 409px; height: 27px;
    border-radius: 14px; background: var(--orange); color: var(--ink);
    font-weight: 700; font-size: 15px; line-height: 27px; text-align: center;
  }
  .deadline {
    position: absolute; top: 587px; left: 0; width: 466px; text-align: center;
    font-weight: 700; font-size: 14.5px; line-height: 22px;
  }
  .contact-bar {
    position: absolute; left: 0; top: 615px; width: 466px; height: 45px;
    background: var(--white); color: var(--ink);
    display: flex; align-items: center; justify-content: center; gap: 8px;
    font-size: 16px;
  }
  .contact-phone { font-weight: 600; }
</style>
</head>
<body>
  <main class="flyer">
    <div class="hero-photo" role="img" aria-label="Photo of a red compact tractor with front loader parked on grass in front of autumn trees"></div>

    <svg class="shapes" viewBox="0 0 466 660" aria-hidden="true">
      <path d="M0,210 C80,262 220,276 466,292 L466,660 L0,660 Z" fill="#252525"/>
      <path d="M0,222 C90,272 230,284 466,300 L466,292 C220,276 80,262 0,210 Z" fill="#9a9a9a"/>
      <path d="M0,186 C45,240 180,262 466,278 L466,292 C220,276 80,262 0,210 Z" fill="#f7931e"/>
    </svg>

    <div class="brand"><span class="brand-dot"></span>BREVLAND AUCTION</div>

    <h1 class="title title-line1">Large Farm &amp;</h1>
    <div class="title title-line2">Construction</div>
    <div class="subtitle"><span class="subtitle-rule"></span>ONLINE ONLY AUCTION<span class="subtitle-rule"></span></div>

    <div class="feature-photo" role="img" aria-label="Photo of a black rotary tiller attachment with yellow PTO shaft"></div>

    <div class="dates">
      <div class="dates-month">November</div>
      <div class="dates-range">3<sup>rd</sup> Thru 5<sup>th</sup></div>
    </div>

    <div class="closing">
      <div class="closing-label">Bidding Closes:</div>
      <div>November 5<sup>th</sup> at 7:00pm</div>
    </div>

    <div class="consign-band">NOW ACCEPTING CONSIGNMENT</div>

    <div class="stat stat-attachments">
      <div class="stat-number">150+</div>
      <div class="stat-label">Skid Steer<br>Attachments</div>
    </div>
    <div class="stat-divider"></div>
    <div class="stat stat-farm">
      <div class="stat-number">50+</div>
      <div class="stat-label">Pieces of Farm<br>Equipment</div>
    </div>

    <div class="welcome-pill">More To Come Consignments are Welcomed</div>
    <div class="deadline">Till October 25Th</div>

    <div class="contact-bar">
      <span class="contact-phone">(555)-271-6038</span>
      <span>|</span>
      <span class="contact-email">Marcus@brevlandsales.com</span>
    </div>
  </main>
</body>
</html>
```